business card for a shoe shop

we would like a business card for a family owned shoe shop.
With this information included.
Darnell's Shoe Store
Family owned since 1947

then on other side
Darnell's Shoe Store
Footwear fitting specialist
Phone: 9187 2630
218 Quarry St, Fernleigh Downs 3187
(cnr. Hartwick Rd and Quarry St)
darnellshoes218@examplemail.com
if could incorporate the purple color on card i have attached.

```html
<!DOCTYPE html>
<html lang="en">
<head>
<meta charset="utf-8">
<title>Darnell's Shoe Store – Business Card</title>
<link rel="stylesheet" href="https://fonts.googleapis.com/css2?family=Poppins:wght@400;500;600;700&display=swap">
<style>
  :root {
    --purple: #7b3be3;
    --purple-light: #a57ae6;
    --paper: #f4f3f2;
    --ink: #111111;
    --white: #ffffff;
    --backdrop: #b3b3b3;
    --icon-border: #d9b98a;
  }
  * { box-sizing: border-box; margin: 0; padding: 0; }
  html, body { width: 731px; height: 1200px; overflow: hidden; }
  body {
    background: var(--backdrop);
    font-family: "Poppins", sans-serif;
    position: relative;
  }
  .card {
    position: absolute;
    top: 338px;
    width: 300px;
    height: 524px;
    overflow: hidden;
    box-shadow: 0 6px 14px rgba(0,0,0,0.25);
    text-align: center;
  }
  .card--front { left: 40px; }
  .card--back { left: 391px; }
  .card__paper {
    position: absolute; inset: 0;
    background: var(--paper);
  }
  .card__shape { position: absolute; left: 0; top: 0; }
  .brand-mark {
    position: absolute;
    left: 50%;
    width: 92px; height: 92px;
    margin-left: -30px;
    border: 3px solid currentColor;
  }
  .brand-name {
    position: absolute; left: 0; right: 0;
    font-weight: 600;
    font-size: 18px;
    letter-spacing: 0.09em;
    text-transform: uppercase;
  }
  .card--front .brand-mark { top: 78px; color: var(--white); }
  .card--front .brand-name { top: 178px; color: var(--white); }
  .tagline {
    position: absolute; left: 0; right: 0; top: 374px;
    font-weight: 700;
    font-size: 22px;
    line-height: 28px;
    letter-spacing: 0.22em;
    color: var(--ink);
    text-transform: uppercase;
  }
  .accent-bar {
    position: absolute; left: 30px; right: 30px; bottom: 0;
    height: 9px;
    background: var(--purple);
    border-radius: 5px 5px 0 0;
  }
  .card--back .brand-mark { top: 52px; color: var(--purple); }
  .card--back .brand-name { top: 154px; color: var(--purple); }
  .specialty {
    position: absolute; left: 0; right: 0; top: 204px;
    font-size: 16px; line-height: 17px;
    text-transform: uppercase;
  }
  .specialty__main { display: block; color: var(--ink); font-weight: 400; }
  .specialty__accent { display: block; color: var(--purple); font-weight: 600; }
  .contact {
    position: absolute; left: 0; right: 0; top: 291px;
    list-style: none;
    color: var(--white);
    font-size: 14px;
    line-height: 17px;
  }
  .contact__item { margin-bottom: 11px; }
  .contact__email { font-size: 13px; }
  .contact__icon {
    display: block;
    width: 26px; height: 26px;
    margin: 0 auto 3px;
    background: var(--white);
    border: 1.5px solid var(--icon-border);
    border-radius: 4px;
    padding: 5px;
  }
  .contact__icon svg { width: 100%; height: 100%; display: block; }
</style>
</head>
<body>

  <section class="card card--front" aria-label="Card front">
    <div class="card__paper" role="img" aria-label="Light grey geometric line pattern background"></div>
    <svg class="card__shape" width="300" height="524" viewBox="0 0 300 524" aria-hidden="true">
      <defs>
        <radialGradient id="frontGlow" cx="0.6" cy="0.42" r="0.6">
          <stop offset="0" stop-color="#a57ae6"/>
          <stop offset="1" stop-color="#7b3be3"/>
        </radialGradient>
      </defs>
      <path d="M0 0 H300 V243 C260 290 200 304 150 304 C100 304 40 290 0 243 Z" fill="url(#frontGlow)"/>
    </svg>
    <div class="brand-mark" aria-hidden="true"></div>
    <h1 class="brand-name">Darnell's Shoe Store</h1>
    <p class="tagline">Family Owned<br>Since 1947</p>
    <div class="accent-bar"></div>
  </section>

  <section class="card card--back" aria-label="Card back">
    <div class="card__paper" role="img" aria-label="Light grey geometric line pattern background"></div>
    <svg class="card__shape" width="300" height="524" viewBox="0 0 300 524" aria-hidden="true">
      <path d="M0 320 C40 278 95 258 150 258 C205 258 260 278 300 320 V524 H0 Z" fill="var(--purple)"/>
    </svg>
    <div class="brand-mark" aria-hidden="true"></div>
    <h2 class="brand-name">Darnell's Shoe Store</h2>
    <p class="specialty">
      <span class="specialty__main">Footwear Fitting</span>
      <span class="specialty__accent">Specialist</span>
    </p>
    <ul class="contact">
      <li class="contact__item">
        <span class="contact__icon" aria-hidden="true">
          <svg viewBox="0 0 24 24"><path d="M6.6 10.8a15 15 0 0 0 6.6 6.6l2.2-2.2c.3-.3.7-.4 1-.2 1.1.4 2.3.6 3.6.6.6 0 1 .4 1 1V20c0 .6-.4 1-1 1A17 17 0 0 1 3 4c0-.6.4-1 1-1h3.5c.6 0 1 .4 1 1 0 1.3.2 2.5.6 3.6.1.3 0 .7-.2 1z" fill="#111"/></svg>
        </span>
        9187 2630
      </li>
      <li class="contact__item contact__email">
        <span class="contact__icon" aria-hidden="true">
          <svg viewBox="0 0 24 24"><rect x="3" y="6" width="18" height="12" fill="#111"/><path d="M3 6l9 7 9-7" fill="none" stroke="#fff" stroke-width="1.5"/></svg>
        </span>
        darnellshoes218@examplemail.com
      </li>
      <li class="contact__item">
        <span class="contact__icon" aria-hidden="true">
          <svg viewBox="0 0 24 24"><path d="M12 2a7 7 0 0 0-7 7c0 5 7 13 7 13s7-8 7-13a7 7 0 0 0-7-7z" fill="#111"/><circle cx="12" cy="9" r="2.6" fill="#fff"/></svg>
        </span>
        218 Quarry St, Fernleigh Downs<br>3187<br>(cnr. Hartwick Rd and Quarry St)
      </li>
    </ul>
  </section>

</body>
</html>
```